Home Page Redesign for Pet Website

Looking to redesign the home page of our WORDPRESS website which will be renamed The Critter Cover Handbook 2015.

Looking for clean design which communicates clarity.
Updates

This is for a Wordpress site.

Please note that the design MUST include the content which is shown in the table in the brief!

Hi Thanks for the designs so far. We have just updated the brief to provide more information and clarify a few issues. We have also now included a couple of layout suggestions. They are just suggestions but it should give you a better idea of what we are looking for. And we have just increased the budget for 1st place by £120. Please feel free to message me if you have any questions. Many thanks. Maud

Please note that the new brief is in a file dated 25 Jan!

Reason: We have extended the deadline so we can continue working with the designers who have submitted designs we like. If you have any new designs please submit them by the original deadline of 7.37pm this evening (GMT). We are planning to make our final decision by Friday this week.

Target Market(s)

UK pet owners. All ages but largest age group is 35-50.

Industry/Entity Type

Insurance

Requirements
Must have
• Three clear content groups - LEARN, RESEARCH, CAMPAIGN (see brief for more details).
Stock photos with dogs and cats
Use current colour scheme
Must work with existing inner pages.
Existing font.. but 1pt larger
See brief for more details
Should not have
• Logo
Content from Existing Page (except for footer content... and menu headings).

```html
<!DOCTYPE html>
<html lang="en">
<head>
<meta charset="utf-8">
<title>The Critter Cover Handbook 2015</title>
<link href="https://fonts.googleapis.com/css2?family=Open+Sans:wght@400;600;700&display=swap" rel="stylesheet">
<style>
:root{
  --orange:#f07c1c;
  --orange-dark:#d9650e;
  --green:#3a9a4a;
  --blue:#2a85c9;
  --purple:#8b3cc0;
  --teal-green:#2f8a55;
  --ink:#333;
  --muted:#666;
  --panel:#f2f2f2;
  --line:#dcdcdc;
  --footer:#2b2624;
  --footer-bottom:#1f1b1a;
  --bio-bar:#2a2422;
}
*{box-sizing:border-box;margin:0;padding:0}
html,body{width:1200px;height:2571px;overflow:hidden;background:#fff;font-family:"Open Sans",Arial,sans-serif;color:var(--ink)}
.page{position:relative;width:1200px;height:2571px}
.abs{position:absolute}

/* hero */
.hero{left:0;top:0;width:1200px;height:629px;background:linear-gradient(180deg,#b8956c 0%,#a98660 55%,#8c6a48 80%,#c2a280 100%)}
.hero-animals{left:780px;top:90px;width:420px;height:470px;border-radius:40px;background:radial-gradient(ellipse at 60% 45%,#f2ede6 0%,#e3d6c5 45%,rgba(169,134,96,0) 75%)}
.brand{left:111px;top:60px;width:266px;font-size:25px;font-weight:700;color:#4a3420;line-height:1.2;text-align:center}
.call{left:852px;top:0;width:240px;height:75px;background:var(--orange);color:#fff;padding:13px 14px;font-size:16px;font-weight:600;line-height:1.35;box-shadow:0 3px 6px rgba(0,0,0,.25);white-space:nowrap}
.call span{display:block;font-size:14px}
.tagline{left:123px;top:253px;font-size:27px;font-weight:600;color:#2a1e14;line-height:1.35}
.search{left:108px;top:345px;width:511px;height:78px;background:rgba(40,30,25,.85);padding:17px}
.search .field{position:absolute;top:17px;height:44px;background:#fff;font-size:12px;color:#999;padding:14px 0 0 40px}
.search .f1{left:17px;width:171px;border-right:1px solid #ddd}
.search .f2{left:188px;width:172px}
.search svg{position:absolute;left:14px;top:13px}
.search .go{position:absolute;left:372px;top:17px;width:123px;height:44px;background:var(--green);color:#fff;font-size:16px;font-weight:600;text-align:center;line-height:44px}

/* nav */
.nav{left:0;top:629px;width:1200px;height:53px;background:var(--orange);border-bottom:3px solid var(--orange-dark)}
.nav ul{list-style:none;position:absolute;left:108px;top:0;display:flex;height:50px}
.nav li{color:#fff;font-size:14px;font-weight:600;padding:0 20px;line-height:50px;border-right:1px solid rgba(255,255,255,.25)}
.nav li.active{background:var(--orange-dark)}
.social{position:absolute;left:958px;top:13px;display:flex;gap:9px}
.social i{display:block;width:26px;height:26px;border-radius:50%;background:#f59a4e;border:1px solid #f8b57b}

/* cards */
.card{top:705px;width:315px;height:695px;background:var(--panel);border:1px solid var(--line)}
.card .photo{height:204px;border-top:5px solid}
.c1{left:108px}.c1 .photo{border-color:var(--blue);background:linear-gradient(135deg,#2f4a3c,#1d3a2c 60%,#6b7c6e)}
.c2{left:442px}.c2 .photo{border-color:var(--purple);background:linear-gradient(135deg,#f4f4f4,#dcd2c8 60%,#f0f0f0)}
.c3{left:777px}.c3 .photo{border-color:var(--teal-green);background:linear-gradient(135deg,#fafafa,#e6ddd2 50%,#f5f5f5)}
.card .head{position:relative;height:80px;padding:14px 0 0 85px}
.card .badge{position:absolute;left:12px;top:12px;width:65px;height:65px;border-radius:50%;display:flex;align-items:center;justify-content:center}
.card h2{font-size:19px;font-weight:600;line-height:1.1}
.card h3{font-size:17px;font-weight:400;line-height:1.3}
.c1 h2,.c1 h3{color:var(--blue)}.c1 .badge{background:var(--blue)}
.c2 h2,.c2 h3{color:var(--purple)}.c2 .badge{background:var(--purple)}
.c3 h2,.c3 h3{color:var(--teal-green)}.c3 .badge{background:var(--teal-green)}
.card .body{padding:8px 11px;font-size:12.5px;color:#444;line-height:1.75}
.links{list-style:none}
.links li{height:44px;line-height:44px;font-size:12.5px;letter-spacing:-.2px;white-space:nowrap}
.providers{display:grid;grid-template-columns:1fr 1fr;margin:12px 0 14px;list-style:none}
.providers li{font-size:12.5px;line-height:22px;padding-left:18px;position:relative}
.providers li:before{content:"";position:absolute;left:2px;top:8px;width:7px;height:7px;border-radius:50%;background:#b58ad6}
.body p+p{margin-top:16px}

/* video banner */
.promo{left:108px;top:1440px;width:326px;height:346px;background:var(--orange);color:#fff}
.promo .brand2{position:absolute;left:28px;top:40px;width:270px;font-size:24px;font-weight:700;line-height:1.2;text-align:center;color:#fff}
.promo .badge{position:absolute;left:12px;top:182px;width:65px;height:65px;border-radius:50%;background:var(--blue)}
.promo .promo-head{position:absolute;left:91px;top:190px}
.promo h2{font-size:19px;font-weight:600;line-height:1.15}
.promo h3{font-size:17px;font-weight:400;line-height:1.3}
.promo p{position:absolute;left:12px;top:268px;width:300px;font-size:12.5px;line-height:1.6;color:#ffd9b5}
.video{left:434px;top:1440px;width:656px;height:346px;background:linear-gradient(120deg,#7a8a5a 0%,#8e8a78 35%,#c9bcae 65%,#ece4dd 100%)}
.play{left:700px;top:1552px}

/* bio */
.rule{left:0;top:1826px;width:1200px;height:9px;background:var(--orange)}
.dogs{left:103px;top:1800px;width:368px;height:308px;background:radial-gradient(ellipse at 50% 55%,#c79a5e 0%,#a07a50 35%,#e8e0d6 70%,rgba(255,255,255,0) 80%)}
.bio-bar{left:483px;top:1856px;width:606px;height:37px;background:var(--bio-bar);color:#fff;font-size:17px;font-weight:700;padding-left:10px;line-height:37px}
.bio-title{left:483px;top:1908px;font-size:14px;font-weight:700;color:#222}
.bio-text{left:483px;top:1938px;width:606px;font-size:12px;line-height:18px;letter-spacing:-.1px;color:#555}
.bio-text p+p{margin-top:14px}
.more{left:483px;top:2057px;width:131px;height:40px;background:var(--orange);color:#fff;font-size:15px;font-weight:600;text-align:center;line-height:40px}

/* footer */
.footer{left:0;top:2143px;width:1200px;height:377px;background:var(--footer);color:#fff}
.footer h4{position:absolute;top:56px;font-size:23px;font-weight:400}
.footer h4 b{font-weight:700;font-size:30px}
.disc{position:absolute;left:110px;top:106px;width:272px;font-size:13px;line-height:1.6;color:#b0a9a5}
.feed{position:absolute;top:116px;width:290px;list-style:none}
.feed li{position:relative;height:78px;padding-left:75px}
.feed .thumb{position:absolute;left:0;top:0;width:64px;height:56px;background:linear-gradient(135deg,#c8b04a,#8c7a3c);border:3px solid #4a4240}
.feed strong{display:block;font-size:11.5px;font-weight:700;line-height:1.3;padding-top:4px}
.feed small{font-size:9px;color:#999}
.bottom{left:0;top:2520px;width:1200px;height:51px;background:var(--footer-bottom);color:#aaa;font-size:13.5px;line-height:51px}
.bottom .copy{position:absolute;left:110px}
.bottom .legal{position:absolute;right:110px}
</style>
</head>
<body>
<div class="page">

  <header>
    <div class="abs hero" role="img" aria-label="Photo of a kitten and a white puppy sitting on a wooden floor against a warm brown wall"></div>
    <div class="abs hero-animals" role="img" aria-label="Kitten and puppy"></div>
    <div class="abs brand">The Critter Cover Handbook 2015</div>
    <div class="abs call">Call Us Now:<span>01632 960118 / 01632 960119</span></div>
    <h1 class="abs tagline">Independent Unbiased Information<br>For Fellow Pet Owners:</h1>
    <form class="abs search">
      <div class="field f1"><svg width="16" height="16" viewBox="0 0 16 16"><rect x="3" y="2" width="10" height="12" fill="none" stroke="#bbb" stroke-width="1.5"/></svg>Select a company</div>
      <div class="field f2"><svg width="16" height="16" viewBox="0 0 16 16"><path d="M8 1a5 5 0 0 1 5 5c0 4-5 9-5 9S3 10 3 6a5 5 0 0 1 5-5z" fill="none" stroke="#bbb" stroke-width="1.5"/><circle cx="8" cy="6" r="1.8" fill="#bbb"/></svg>Select a Policy</div>
      <div class="go">SEARCH NOW</div>
    </form>
  </header>

  <nav class="abs nav">
    <ul>
      <li class="active">Home</li>
      <li>Pet Insurance Reviews</li>
      <li>Providers A-Z</li>
      <li>Pet Insurance Policies</li>
      <li>Surveys</li>
      <li>More</li>
    </ul>
    <div class="social"><i></i><i></i><i></i><i></i></div>
  </nav>

  <section class="abs card c1">
    <div class="photo" role="img" aria-label="Dog wearing glasses holding colourful books in front of a chalkboard"></div>
    <div class="head">
      <div class="badge"><svg width="34" height="34" viewBox="0 0 34 34"><path d="M4 17L17 5l13 12M8 14v14h18V14" fill="none" stroke="#fff" stroke-width="3"/></svg></div>
      <h2>LEARN</h2><h3>About Pet Insurance</h3>
    </div>
    <ul class="body links">
      <li>Introduction to Pet Insurance</li>
      <li>Vet Fees Cover Types</li>
      <li>What to Consider before Buying</li>
      <li>Ten Popular Pet Insurance Providers</li>
      <li>Confused by Pet Insurance:&nbsp; Start Here!</li>
      <li>Third Party Liability Insurance</li>
      <li>Six Vet Fees Pet Insurance Companies Won't Pay!</li>
      <li>Why Cheap Pet Insurance is Risky</li>
      <li>Why Your Pets Vet History is Important</li>
    </ul>
  </section>

  <section class="abs card c2">
    <div class="photo" role="img" aria-label="Vet in a white coat holding a small white dog"></div>
    <div class="head">
      <div class="badge"><svg width="34" height="34" viewBox="0 0 34 34"><circle cx="14" cy="14" r="9" fill="none" stroke="#fff" stroke-width="3"/><path d="M21 21l8 8" stroke="#fff" stroke-width="4"/></svg></div>
      <h2>RESEARCH</h2><h3>UK Pet Insurance Policies</h3>
    </div>
    <div class="body">
      <p>Analysis, Customer Reviews and Full Details of All UK Policies</p>
      <ul class="providers">
        <li>Furrow Friends</li><li>Kennel Circle</li>
        <li>Arcton</li><li>R&amp;T</li>
        <li>Straight Path</li><li>Much More</li>
        <li>B&amp;K</li><li>Pawplan</li>
        <li>Hale Paws</li><li>Saltbury's</li>
        <li>Helpwell</li><li>Tesmo</li>
        <li>Jon Lowry</li><li>Vernon Money</li>
        <li>QV=</li><li>Other Providers</li>
      </ul>
      <p>Search our database for policies matching your criteria</p>
      <p>Compare claims experiences for pet insurance providers</p>
    </div>
  </section>

  <section class="abs card c3">
    <div class="photo" role="img" aria-label="Terrier dog shouting into a megaphone"></div>
    <div class="head">
      <div class="badge"><svg width="34" height="34" viewBox="0 0 34 34"><path d="M6 13h6l12-7v22l-12-7H6z" fill="#fff"/><path d="M10 21l2 8" stroke="#fff" stroke-width="3"/></svg></div>
      <h2>CAMPAIGN</h2><h3>For Fairer Pet Insurance</h3>
    </div>
    <div class="body">
      <p>Lorem ipsum dolor sit amet, consectetur adipiscing elit, sed do eiusmod tempor incididunt ut labore et dolore magna aliqua ut enim ad minim veniam, quis nostrud exercitation ullamco laboris nisi ut aliquip ex ea commodo consequat.</p>
      <p>Duis aute irure dolor in reprehenderit in voluptate velit ullamco laboris nisi ut aliquip ex ea commodo consequat esse cillum dolore eu fugiat nulla pariatur lorem ipsum dolor sit amet, consectetur adipiscing elit, sed do eiusmod tempor incididunt ut labore et dolore magna aliqua.</p>
      <p>Ut enim ad minim veniam, quis nostrud exercitation ullamco laboris nisi ut aliquip ex ea commodo consequat.</p>
    </div>
  </section>

  <section class="abs promo">
    <div class="brand2">The Critter Cover Handbook 2015</div>
    <div class="badge"></div>
    <div class="promo-head">
      <h2>POPULAR RESOURCES</h2>
      <h3>About Pet Insurance</h3>
    </div>
    <p>Lorem ipsum dolor sit amet consectetur adipiscing elit, Sed do euismod tempor incidunt ut labore et dolore magna aliqua..</p>
  </section>
  <div class="abs video" role="img" aria-label="Video still of a smiling girl lying in the grass with a tabby cat"></div>
  <svg class="abs play" width="130" height="130" viewBox="0 0 130 130" aria-hidden="true">
    <circle cx="65" cy="65" r="60" fill="rgba(255,255,255,.55)" stroke="#e6e6e6" stroke-width="4"/>
    <path d="M50 38l40 27-40 27z" fill="#2a85c9"/>
  </svg>

  <div class="abs rule"></div>
  <div class="abs dogs" role="img" aria-label="Four dogs sitting together: a collie, a golden retriever, a terrier and a small terrier"></div>
  <div class="abs bio-bar">BIO</div>
  <div class="abs bio-title">LOREM IPSUM&nbsp; DOLOR SIT AMET</div>
  <div class="abs bio-text">
    <p>Lorem ipsum dolor sit amet, consectetur adipiscing elit, sed do eiusmod tempor incididunt ut labore et dolore magna aliqua. Ut enim ad minim veniam, quis nostrud exercitation ullamco laboris nisi ut aliquip ex ea commodo consequat.</p>
    <p>Duis aute irure dolor in reprehenderit in voluptate velit esse cillum dolore eu fugiat nulla pariatur. Excepteur sint occaecat cupidatat non proident, sunt in culpa qui officia deserunt mollit anim id est laborum..</p>
  </div>
  <div class="abs more">READ MORE</div>

  <footer class="abs footer">
    <h4 style="left:110px">Disclaimer</h4>
    <p class="disc">Please note that pet insurance terms often change. Whilst we will do our best to keep this website up to date you must check with the appropriate insurer before making any decisions. If you find any mistakes on this website please do let us know so we can correct it for the benefit of future visitors. Many thanks! -</p>
    <h4 style="left:456px"><b>Pawbook</b> Feeds</h4>
    <ul class="feed" style="left:456px">
      <li><span class="thumb" role="img" aria-label="Dog thumbnail"></span><strong>Phasellus molestie magna non est bibendum non venenatis nisl.</strong><small>Posted on May 21st &nbsp;|&nbsp; 32 Comments</small></li>
      <li><span class="thumb" role="img" aria-label="Dog thumbnail"></span><strong>Phasellus molestie magna non est bibendum non venenatis nisl.</strong><small>Posted on May 21st &nbsp;|&nbsp; 32 Comments</small></li>
      <li><span class="thumb" role="img" aria-label="Dog thumbnail"></span><strong>Phasellus molestie magna non est bibendum non venenatis nisl.</strong><small>Posted on May 21st &nbsp;|&nbsp; 32 Comments</small></li>
    </ul>
    <h4 style="left:819px"><b>Chirper</b> Feeds</h4>
    <ul class="feed" style="left:819px">
      <li><span class="thumb" role="img" aria-label="Dog thumbnail"></span><strong>Phasellus molestie magna non est bibendum non venenatis nisl.</strong><small>Posted on May 21st &nbsp;|&nbsp; 32 Comments</small></li>
      <li><span class="thumb" role="img" aria-label="Dog thumbnail"></span><strong>Phasellus molestie magna non est bibendum non venenatis nisl.</strong><small>Posted on May 21st &nbsp;|&nbsp; 32 Comments</small></li>
      <li><span class="thumb" role="img" aria-label="Dog thumbnail"></span><strong>Phasellus molestie magna non est bibendum non venenatis nisl.</strong><small>Posted on May 21st &nbsp;|&nbsp; 32 Comments</small></li>
    </ul>
  </footer>
  <div class="abs bottom">
    <span class="copy">© 2015. Critter Cover Surveys UK. All Right Reserved.</span>
    <span class="legal">Legal Information &amp; Disclaimers &nbsp;&nbsp;|&nbsp;&nbsp; Privacy Policy</span>
  </div>

</div>
</body>
</html>
```